Chronicles of Kin Logo Design plus business cards design

We are a start up company that will help seniors write their memoirs...beginning with a few ancestors and their heritage and continuing through their own history...how they would like to be remembered in the next generation. I envision a card with a senior citizen at an older writing desk, writing her memoirs, with a book (maybe standing on top, leaning slightly) that has the words Chronicles of Kin.com on the back binding. OR maybe a senior couple walking into the sunset with the same book somewhere in the frame. Communicating the relevance of every life being significant to those that come after them...when a genealogy doesn't say enough about the details of ones life. Please note that I am open to the professionals own ideas...I am not locked into my concepts. On the back of the card I would like one or two phrases..."A Genealogy Doesn't Say Enough" and/or "Every life legacy is uniquely significant to the next generation".
Updates

I have added a couple of photos for ideas that may be used if needed.

I have both increased and committed the payment! Thanks for the reminder!

Reason: We increased the payment commitment and added some photo ideas to help.

We want to thank EVERYONE who participated in this contest. There were so many wonderful and VERY professional proposals...making it very challenging to decide on one! We are posting a new contest for a brochure now and hope many of you will participate. May God bless your endeavors.

Target Market(s)

Senior populous & baby boomer generation.

Industry/Entity Type

Business

Logo Text

Chronicles of Kin quiet years...lasting echoes

Requirements
Must have
• Relevant info:
Domain name: chroniclesofkin.com
email: info@chroniclesofkin.com
phone: 1-855-KIN-TALE toll free
1-717-382-6150 local
name: Doris Halvorsen, M.A.
Nice to have
• photo of senior or senior couple....book with our web address on the binding. I attached two photos that could work if cropped and enhanced. Words need to be deleted from the one photo of senior at a writing desk and couple on the beach could use a sunset sky and other people cropped out. Just ideas...don't know if you have better ones or prefer a different idea.

```html
<!DOCTYPE html>
<html lang="en">
<head>
<meta charset="utf-8">
<title>Chronicles of Kin — Business Card</title>
<link href="https://fonts.googleapis.com/css2?family=Arimo:wght@400;700&display=swap" rel="stylesheet">
<style>
  :root {
    --page: #ece7e1;
    --card-light: #bb8c64;
    --card-mid: #9c6c47;
    --card-deep: #7a5032;
    --band: #2a1710;
    --ink-dark: #2a1710;
    --ink-light: #ffffff;
    --art-light: #8a6a5a;
    --art-dark: #3a2218;
  }
  * { box-sizing: border-box; margin: 0; padding: 0; }
  html, body { width: 1200px; height: 1000px; overflow: hidden; }
  body {
    background: var(--page);
    font-family: "Arimo", Arial, sans-serif;
    position: relative;
  }
  .card {
    position: absolute;
    left: 180px;
    width: 840px;
    height: 470px;
    border-radius: 34px;
    overflow: hidden;
    background:
      radial-gradient(ellipse 120% 110% at 0% 60%, var(--card-light) 0%, var(--card-mid) 55%, var(--card-deep) 100%);
    box-shadow: 0 6px 18px rgba(60, 35, 20, 0.25);
  }
  .card--front { top: 20px; }
  .card--back  { top: 510px; }

  .card-backdrop {
    position: absolute;
    inset: 0;
    background: radial-gradient(circle at 0% 55%, rgba(255, 235, 210, 0.18) 0%, rgba(255, 235, 210, 0) 60%);
  }

  .band {
    position: absolute;
    left: 0; bottom: 0;
    width: 100%;
    height: 110px;
  }
  .band-text {
    position: absolute;
    color: var(--ink-light);
    font-size: 22px;
    letter-spacing: 0.5px;
    white-space: nowrap;
  }

  /* Front */
  .reader-art {
    position: absolute;
    left: 330px; top: 40px;
    width: 190px; height: 220px;
    border-radius: 90px 90px 60px 60px;
    background: linear-gradient(180deg, var(--art-light), var(--art-dark));
  }
  .front-wordmark {
    position: absolute;
    left: 110px; top: 282px;
    font-size: 54px;
    font-weight: 700;
    color: var(--ink-light);
    letter-spacing: -0.5px;
    white-space: nowrap;
  }
  .front-url { left: 0; right: 0; bottom: 30px; text-align: center; }

  /* Back */
  .couple-art {
    position: absolute;
    left: 130px; top: 130px;
    width: 320px; height: 340px;
    border-radius: 120px 120px 0 0;
    background: linear-gradient(180deg, #4a2a1c, var(--art-dark));
  }
  .back-wordmark {
    position: absolute;
    right: 44px; top: 36px;
    font-size: 40px;
    font-weight: 700;
    color: var(--ink-dark);
    white-space: nowrap;
  }
  .holder-name {
    position: absolute;
    left: 480px; top: 140px;
    font-size: 30px;
    font-weight: 700;
    color: var(--ink-light);
    white-space: nowrap;
  }
  .contact-list {
    position: absolute;
    left: 480px; top: 200px;
    list-style: none;
  }
  .contact-item {
    display: flex;
    align-items: center;
    gap: 10px;
    font-size: 22px;
    font-weight: 700;
    color: var(--ink-light);
    margin-bottom: 8px;
    white-space: nowrap;
  }
  .contact-icon {
    width: 24px; height: 24px;
    border-radius: 50%;
    background: var(--band);
    border: 1.5px solid var(--card-light);
    display: flex; align-items: center; justify-content: center;
  }
  .toll-free { right: 80px; bottom: 28px; font-weight: 700; }
</style>
</head>
<body>

<section class="card card--front">
  <div class="card-backdrop" role="img" aria-label="Soft warm sunburst backdrop"></div>
  <div class="reader-art" role="img" aria-label="Illustration of a senior woman seated in an armchair reading a book"></div>
  <p class="front-wordmark">chroniclesofkin.com</p>
  <svg class="band" viewBox="0 0 840 110" preserveAspectRatio="none" aria-hidden="true">
    <path d="M0 60 Q420 0 840 30 L840 110 L0 110 Z" fill="var(--band)"/>
  </svg>
  <p class="band-text front-url">www.chroniclesofkin.com</p>
</section>

<section class="card card--back">
  <div class="card-backdrop" role="img" aria-label="Soft warm sunburst backdrop"></div>
  <p class="back-wordmark">chroniclesofkin.com</p>
  <div class="couple-art" role="img" aria-label="Silhouette illustration of a senior couple walking arm in arm"></div>
  <p class="holder-name">Doris Halvorsen, M.A.</p>
  <ul class="contact-list">
    <li class="contact-item">
      <span class="contact-icon">
        <svg width="14" height="14" viewBox="0 0 24 24" aria-hidden="true"><path fill="#fff" d="M6.6 10.8a15 15 0 0 0 6.6 6.6l2.2-2.2a1 1 0 0 1 1-.25 11.4 11.4 0 0 0 3.6.57 1 1 0 0 1 1 1V20a1 1 0 0 1-1 1A17 17 0 0 1 3 4a1 1 0 0 1 1-1h3.5a1 1 0 0 1 1 1c0 1.25.2 2.45.57 3.6a1 1 0 0 1-.25 1z"/></svg>
      </span>
      1-717-382-6150
    </li>
    <li class="contact-item">
      <span class="contact-icon">
        <svg width="14" height="14" viewBox="0 0 24 24" aria-hidden="true"><rect x="3" y="6" width="18" height="12" rx="1.5" fill="#fff"/><path d="M3 7l9 6 9-6" stroke="#2a1710" stroke-width="1.6" fill="none"/></svg>
      </span>
      info@chroniclesofkin.com
    </li>
  </ul>
  <svg class="band" viewBox="0 0 840 110" preserveAspectRatio="none" aria-hidden="true">
    <path d="M0 90 Q420 20 840 40 L840 110 L0 110 Z" fill="var(--band)"/>
  </svg>
  <p class="band-text toll-free">1-855-KIN-TALE toll free</p>
</section>

</body>
</html>
```